Nobre Lente Lusitana - business card

Create a business card for my eyewear (glasses) store. The concept is based in handcrafted glasses (as well as common frames and 3d printed), clean, and elegant. The business card could be black (white letters and symbols) or white (black letters and symbols) but we are open to new suggestions. It must be sober and elegant.
The name Nobre Lente Lusitana means Royal/Real Portuguese Optical Store.
Our concept should be inspired by the pictures attatched bellow.
I would like it to be classic and elegant as business cards for bankers.
Our first selected logo is also available in attachment files.

Target Market(s)

For business meetings with investors, supliers and fairs

Industry/Entity Type

Eyewear

Contact Information for Business Card

Some random business cards in attachment that we like. Don't be closed to it, we like freedom of think.

Font styles to use
Serif
Sans Serif

Colors
404040
e9e9e9
fbfbfb
000000
85abd3
0255a3
f7fbfd
959595

Requirements
Must have
• Must be elegant, simple.
• Must present our brand new logo (slight variations are welcome, the logo is not closed yet). See our temporary logo in attachment.
• Black (or dark grey), white (or light grey) and a third slight color.
• This third slight color could be dark blue or grayish blue.
• Info:
• Fernando Amaral (name)
• famaral@nobrelentelusitana.example
• +351 936204518
• www.nobrelentelusitana.example
Nice to have
• Black and white or with serious colors such as dark blue or greyish blue.
• Could also have water mark with our logo (big size) in the background (inspired in KVN bank credit card design)
Should not have
• Hysteric colora or shapes

```html
<!DOCTYPE html>
<html lang="pt">
<head>
<meta charset="utf-8">
<title>Nobre Lente Lusitana – Business Card</title>
<link rel="stylesheet" href="https://fonts.googleapis.com/css2?family=Bebas+Neue&family=Josefin+Sans:wght@400&family=Open+Sans:wght@400&display=swap">
<style>
  :root {
    --backdrop: #e9e9e9;
    --card-dark: #2a2a2b;
    --card-light: #fbfbfb;
    --ink: #000000;
    --ink-soft: #1a1a1a;
    --metal: #959595;
    --rule: #404040;
  }
  * { margin: 0; padding: 0; box-sizing: border-box; }
  html, body { width: 1200px; height: 1000px; overflow: hidden; }
  body { background: var(--backdrop); position: relative; }

  .card {
    position: absolute;
    left: 266px;
    width: 666px;
    height: 397px;
    border-radius: 26px;
  }
  .card--front {
    top: 75px;
    background: var(--card-dark);
    display: flex;
    flex-direction: column;
    align-items: center;
    justify-content: center;
    gap: 26px;
  }
  .card--back {
    top: 533px;
    background: var(--card-light);
  }

  .brand-dot {
    width: 18px; height: 18px;
    border-radius: 50%;
    background: var(--metal);
  }
  .brand-name {
    font-family: "Josefin Sans", sans-serif;
    font-weight: 400;
    color: var(--metal);
    text-transform: uppercase;
    text-align: center;
    font-size: 29px;
    letter-spacing: 3px;
    line-height: 1.3;
  }

  .holder {
    position: absolute;
    right: 398px;
    top: 170px;
    text-align: right;
  }
  .holder__name {
    font-family: "Bebas Neue", sans-serif;
    font-size: 30px;
    line-height: 1;
    color: var(--ink);
    letter-spacing: 0.3px;
  }
  .holder__role {
    font-family: "Open Sans", sans-serif;
    font-size: 15px;
    color: var(--ink-soft);
    margin-top: 4px;
  }
  .divider {
    position: absolute;
    left: 286px;
    top: 170px;
    width: 1.5px;
    height: 56px;
    background: var(--rule);
  }
  .contacts {
    position: absolute;
    left: 302px;
    top: 165px;
    list-style: none;
    font-family: "Open Sans", sans-serif;
    font-size: 16px;
    color: var(--ink-soft);
    line-height: 20.5px;
  }
  .contacts li { display: flex; align-items: center; gap: 7px; }
  .contacts svg { width: 14px; height: 14px; flex: none; }
</style>
</head>
<body>
  <section class="card card--front" aria-label="Card front">
    <span class="brand-dot"></span>
    <p class="brand-name">Nobre Lente<br>Lusitana</p>
  </section>

  <section class="card card--back" aria-label="Card back">
    <div class="holder">
      <p class="holder__name">FERNANDO AMARAL</p>
      <p class="holder__role">Managing Partner</p>
    </div>
    <span class="divider"></span>
    <ul class="contacts">
      <li>
        <svg viewBox="0 0 16 16" fill="none" stroke="#1a1a1a" stroke-width="1.4"><path d="M3 1.5h3l1.2 3.3-1.8 1.2a8 8 0 0 0 4.6 4.6l1.2-1.8 3.3 1.2v3a1.5 1.5 0 0 1-1.6 1.5A13 13 0 0 1 1.5 3.1 1.5 1.5 0 0 1 3 1.5z"/></svg>
        +351 936204518
      </li>
      <li>
        <svg viewBox="0 0 16 16" fill="none" stroke="#1a1a1a" stroke-width="1.4"><rect x="1" y="3" width="14" height="10"/><path d="M1 3l7 6 7-6"/></svg>
        famaral@nobrelentelusitana.example
      </li>
      <li>
        <svg viewBox="0 0 16 16" fill="none" stroke="#1a1a1a" stroke-width="1.2"><circle cx="8" cy="8" r="6.5"/><ellipse cx="8" cy="8" rx="3" ry="6.5"/><path d="M1.5 8h13M2.5 4.8h11M2.5 11.2h11"/></svg>
        www.nobrelentelusitana.example
      </li>
    </ul>
  </section>
</body>
</html>
```